Design a large parking banner – mandatory ticket validation in the shop

Banner Size:
548 cm (width) x 154 cm (height)
Note: The banner will be placed in a metal frame at our parking lot entrance, fully visible to every incoming truck driver. The message must be easy to read from a distance.
Goal of the Banner:
To inform all truck drivers that they must validate their entry ticket inside the shop, even if they are parking for a short time.
The message must be displayed in multiple languages for international drivers.
Mandatory Content:
Main message – in multiple languages (clearly separated or stacked):
Dutch (NL): Vergeet je ticket niet te valideren in de shop – verplicht, ook bij kort parkeren!
French (FR): N'oubliez pas de valider votre ticket à la boutique – obligatoire, même pour un court arrêt !
English (EN): Don't forget to validate your entry ticket in the shop – mandatory, even for short stops!
German (DE): Vergessen Sie nicht, Ihr Einfahrticket im Shop zu entwerten – Pflicht, auch bei kurzem Parken!
Polish (PL): Nie zapomnij zatwierdzić biletu w sklepie – obowiązkowe, nawet przy krótkim postoju!
Romanian (RO): Nu uitați să validați biletul în magazin – obligatoriu, chiar și pentru opriri scurte!
You can include more languages if space allows, but these are essential.
Opening Hours Block (in one section below):
Shop Opening Hours
Mon – Fri: 05:30 – 22:00
Sat & Sun: 08:00 – 22:00
Style & Branding:
The design must match the visual identity of Haulpoint 41Ter
Please refer to the attached photos of existing parking signage for guidance on colors, typography, and layout style
Our logo (attached) must be clearly visible and professionally integrated
Feel free to use icons or pictograms to visually support the message (e.g., ticket, truck, arrow)
Readability is key – large, bold text and high contrast colors that are visible from a distance
Target Audience:
International truck drivers – people who need fast, clear communication. Not everyone speaks the local language, so visual clarity and multilingual messaging are critical.
File Requirements:
Print-ready file (PDF or EPS) – 300 dpi at 1:10 scale
Include 5 cm bleed on all sides
Provide open source files if possible (AI or PSD)

```html
<!DOCTYPE html>
<html lang="en">
<head>
<meta charset="utf-8">
<title>Ticket validation banner – Haulpoint 41Ter</title>
<link href="https://fonts.googleapis.com/css2?family=Poppins:wght@400;600;700&display=swap" rel="stylesheet">
<style>
  :root {
    --navy: #1f2358;
    --white: #ffffff;
    --red: #d0202e;
    --page: #ffffff;
  }
  html, body {
    margin: 0;
    padding: 0;
    width: 1200px;
    height: 1200px;
    overflow: hidden;
    background: var(--page);
    font-family: "Poppins", sans-serif;
  }
  .banner {
    position: absolute;
    left: 45px;
    top: 444px;
    width: 1260px;
    height: 354px;
    background: var(--navy);
    color: var(--white);
    transform: scale(0.88);
    transform-origin: top left;
    box-shadow: 0 10px 28px rgba(0,0,0,0.35);
  }
  .headline {
    position: absolute;
    left: 30px;
    top: 28px;
    margin: 0;
    font-size: 38px;
    font-weight: 600;
    line-height: 1.1;
    letter-spacing: -0.3px;
    white-space: nowrap;
  }
  .headline-sub {
    position: absolute;
    left: 30px;
    top: 76px;
    margin: 0;
    font-size: 23px;
    font-weight: 400;
  }
  .brand {
    position: absolute;
    right: 26px;
    top: 30px;
    display: flex;
    align-items: center;
    gap: 10px;
  }
  .brand-dot {
    width: 12px;
    height: 12px;
    border-radius: 50%;
    background: var(--white);
    flex: none;
  }
  .brand-name {
    font-size: 24px;
    font-weight: 700;
    line-height: 1.05;
    text-align: right;
  }
  .brand-name span { display: block; }
  .icon-alert {
    position: absolute;
    left: 30px;
    top: 160px;
    width: 72px;
    height: 72px;
  }
  .icon-ticket {
    position: absolute;
    left: 30px;
    top: 262px;
    width: 72px;
    height: 56px;
  }
  .msg {
    position: absolute;
    margin: 0;
  }
  .msg-title {
    display: block;
    font-size: 21px;
    font-weight: 600;
    line-height: 1.2;
  }
  .msg-note {
    display: block;
    font-size: 14px;
    font-weight: 400;
    line-height: 1.3;
  }
  .msg-nl { left: 127px; top: 157px; }
  .msg-fr { left: 127px; top: 219px; }
  .msg-de { left: 127px; top: 281px; }
  .msg-pl { left: 790px; top: 148px; }
  .msg-ro { left: 790px; top: 218px; }
  .hours-rule {
    position: absolute;
    left: 790px;
    top: 276px;
    width: 428px;
    height: 2px;
    background: var(--red);
  }
  .hours-label {
    position: absolute;
    left: 790px;
    top: 289px;
    font-size: 14px;
    font-weight: 400;
    text-transform: uppercase;
  }
  .hours-list {
    position: absolute;
    left: 977px;
    top: 286px;
    margin: 0;
    padding: 0;
    list-style: none;
    font-size: 16px;
    font-weight: 700;
    line-height: 23px;
  }
</style>
</head>
<body>
  <section class="banner">
    <h1 class="headline">Don't forget to validate your entry ticket in the shop</h1>
    <p class="headline-sub">mandatory, even for short stops!</p>

    <div class="brand">
      <span class="brand-dot"></span>
      <div class="brand-name"><span>Haulpoint</span><span>41Ter</span></div>
    </div>

    <svg class="icon-alert" viewBox="0 0 72 72" aria-hidden="true">
      <circle cx="36" cy="36" r="36" fill="#ffffff"/>
      <rect x="32" y="17" width="8" height="26" rx="2" fill="#1f2358"/>
      <rect x="32" y="48" width="8" height="8" rx="2" fill="#1f2358"/>
    </svg>

    <svg class="icon-ticket" viewBox="0 0 72 56" aria-hidden="true">
      <path d="M46 2 L56 8 L54 13 L42 13 Z" fill="#ffffff"/>
      <rect x="28" y="12" width="30" height="8" fill="#ffffff"/>
      <path d="M0 22 H72 V30 H66 V38 H72 V46 H0 V38 H6 V30 H0 Z" fill="#ffffff"/>
      <rect x="20" y="28" width="22" height="12" fill="#1f2358"/>
      <rect x="46" y="28" width="6" height="12" fill="#1f2358"/>
      <rect x="0" y="48" width="72" height="8" fill="#ffffff"/>
    </svg>

    <p class="msg msg-nl">
      <span class="msg-title">Vergeet je ticket niet te valideren in de shop</span>
      <span class="msg-note">verplicht, ook bij kort parkeren!</span>
    </p>
    <p class="msg msg-fr">
      <span class="msg-title">N'oubliez pas de valider votre ticket à la boutique</span>
      <span class="msg-note">obligatoire, même pour un court arrêt !</span>
    </p>
    <p class="msg msg-de">
      <span class="msg-title">Vergessen Sie nicht, Ihr Einfahrticket im Shop zu entwerten</span>
      <span class="msg-note">Pflicht, auch bei kurzem Parken!</span>
    </p>
    <p class="msg msg-pl">
      <span class="msg-title">Nie zapomnij zatwierdzić biletu w sklepie</span>
      <span class="msg-note">obowiązkowe, nawet przy krótkim postoju!</span>
    </p>
    <p class="msg msg-ro">
      <span class="msg-title">Nu uitați să validați biletul în magazin</span>
      <span class="msg-note">obligatoriu, chiar și pentru opriri scurte!</span>
    </p>

    <div class="hours-rule"></div>
    <div class="hours-label">Shop opening hours:</div>
    <ul class="hours-list">
      <li>Mon – Fri: 05:30 – 22:00</li>
      <li>Sat &amp; Sun: 08:00 – 22:00</li>
    </ul>
  </section>
</body>
</html>
```